Fitness Facility needs a Flyer!

We need a flyer that highlights our 3 different fitness programs.
During the sales process, we'd like to have a visual reference for new prospective clients that highlights our 3 different fitness programs.
The flyer should be colorful, Focus on the different fitness programs BUT! We'd like to steer people towards our middle program, so I'd like the middle program "The Grand Sleek & Shaped Makeover" to be possibly a little larger than the two others so that the eye naturally gravitates towards that one.
I'd like the flyer to be in a Landscape layout,
Include our logo
Include a group photo of our team
Include the text "Most Popular" over the middle program
Include the text "Save More - 10% discount if paid in full" at the very bottom of the page
I have attached the text of our programs, a group photo, our logo and an example of our last program ... just as an example and not to be duplicated.
Look and feel
Each slider illustrates characteristics of the customer's brand and the style your logo design should communicate.

```html
<!DOCTYPE html>
<html lang="en">
<head>
<meta charset="utf-8">
<title>FitKorva Programs Flyer</title>
<link rel="stylesheet" href="https://fonts.googleapis.com/css2?family=Barlow:wght@400;500;700&family=Kaushan+Script&family=Caveat+Brush&display=swap">
<style>
  :root {
    --sky: #379dd8;
    --ink: #121212;
    --gold: #f0bd2c;
    --white: #ffffff;
    --body-font: "Barlow", Arial, sans-serif;
    --script-font: "Kaushan Script", "Brush Script MT", cursive;
    --price-font: "Caveat Brush", "Brush Script MT", cursive;
  }
  * { margin: 0; padding: 0; box-sizing: border-box; }
  html, body { width: 1200px; height: 848px; overflow: hidden; background: var(--sky); }
  .flyer {
    position: relative; width: 1200px; height: 848px; overflow: hidden;
    background: var(--sky); font-family: var(--body-font); color: var(--white);
  }
  .panels { position: absolute; inset: 0; }
  .panel-fill { fill: var(--ink); }

  .tier-number, .tier-name, .popular-tag, .price {
    position: absolute; line-height: 1; white-space: nowrap;
  }
  .tier-number, .tier-name, .popular-tag { font-family: var(--script-font); color: var(--gold); font-weight: 400; }

  .tier-number--one { left: 30px; top: 46px; font-size: 110px; }
  .tier-name--one { left: 74px; top: 98px; font-size: 32px; }

  .tier-number--two { left: 318px; top: 20px; font-size: 190px; }
  .popular-tag { left: 442px; top: 32px; font-size: 66px; }
  .tier-name--two { left: 436px; top: 136px; font-size: 39px; line-height: 1.22; white-space: normal; width: 350px; }
  .tier-name--two .first-line { padding-left: 20px; }

  .tier-number--three { left: 850px; top: 38px; font-size: 104px; }
  .tier-name--three { left: 918px; top: 88px; font-size: 28px; }

  .features { position: absolute; list-style: none; font-weight: 400; }
  .features li::before { content: "\25AA\00A0"; }
  .features .lead { font-weight: 700; }
  .features--one { left: 29px; top: 196px; width: 300px; font-size: 17.5px; line-height: 20.5px; }
  .features--two { left: 390px; top: 272px; width: 400px; font-size: 19.5px; line-height: 23.3px; }
  .features--three { left: 842px; top: 194px; width: 348px; font-size: 19.5px; line-height: 23.9px; }

  .price { font-family: var(--price-font); color: var(--white); }
  .price .amount { color: var(--gold); }
  .price .tick { color: var(--sky); font-size: 0.7em; vertical-align: top; }
  .price--one { left: 22px; top: 362px; font-size: 52px; }
  .price--two { left: 400px; top: 632px; font-size: 58px; }
  .price--three { left: 880px; top: 498px; font-size: 54px; }
  .price--two .tick { color: var(--gold); }

  .footer {
    position: absolute; left: 0; right: 0; top: 772px; text-align: center; font-weight: 700;
  }
  .footer-offer { font-size: 17.4px; line-height: 28px; }
  .footer-tagline { font-size: 17.4px; line-height: 30px; }
</style>
</head>
<body>
<main class="flyer">
  <svg class="panels" width="1200" height="848" viewBox="0 0 1200 848" aria-hidden="true">
    <path class="panel-fill" d="M0 0 H362 L352 20 L344 18 L346 40 L336 52 L340 78 L332 96 L338 118 L328 140 L336 168 L330 196 L338 222 L332 250 L342 276 L336 300 L346 330 L340 356 L352 384 L348 410 L360 440 L354 468 L366 496 L362 524 L374 552 L370 580 L382 606 L378 634 L390 660 L388 690 L398 716 L396 742 L410 760 L404 778 L300 772 L200 780 L100 772 L0 778 Z"/>
    <path class="panel-fill" d="M800 0 H1200 V740 L1120 746 L1040 740 L960 748 L880 744 L836 752 L826 732 L832 710 L818 690 L824 660 L810 636 L816 606 L804 580 L810 550 L798 520 L804 490 L792 462 L800 432 L786 404 L794 374 L782 346 L790 316 L778 288 L788 258 L776 230 L786 200 L776 172 L788 144 L780 116 L792 88 L786 60 L798 34 L792 14 Z"/>
  </svg>

  <section class="tier tier--one">
    <span class="tier-number tier-number--one">1</span>
    <h2 class="tier-name tier-name--one">Trim Frame Start</h2>
    <ul class="features features--one">
      <li>4 Group Training Sessions per week</li>
      <li>Customized Meal Plan</li>
      <li>Monthly BodyScope Scans</li>
      <li>Supplement List</li>
      <li>Access to Private FitKorva ClubSpace Group</li>
    </ul>
    <p class="price price--one"><span class="tick">&#8220;</span><span class="amount">$47</span> per week<span class="tick">&#8221;</span></p>
  </section>

  <section class="tier tier--two">
    <span class="tier-number tier-number--two">2</span>
    <p class="popular-tag">Most Popular!</p>
    <h2 class="tier-name tier-name--two"><span class="first-line">The Grand Sleek</span><br>&amp; Shaped Makeover</h2>
    <ul class="features features--two">
      <li class="lead">UNLIMITED Group Training Sessions Designed to Sculpt &amp; Tone the body</li>
      <li>Customized AND Phased Nutrition Plans so your metabolism never plateaus</li>
      <li>Your own Accountability Coach who will be your biggest cheerleader and motivator</li>
      <li>Weekly accountability Check In’s</li>
      <li>Bi-weekly 1-on-1 accountability &amp; strategy meetups</li>
      <li>Bi-weekly BodyScope Scans</li>
      <li>Supplement List to accelerate metabolism</li>
      <li>Exclusive access to FitKorva’s Private ClubSpace Page for additional Recipes, Support and Guidance</li>
    </ul>
    <p class="price price--two"><span class="tick">&#8220;</span>Only <span class="amount">$69</span> per week<span class="tick">&#8221;</span></p>
  </section>

  <section class="tier tier--three">
    <span class="tier-number tier-number--three">3</span>
    <h2 class="tier-name tier-name--three">1-On-1 Power Sprint</h2>
    <ul class="features features--three">
      <li class="lead">(8) 1-on-1 Personal Training Sessions per month</li>
      <li>UNLIMITED Group Training Sessions</li>
      <li>Customized AND Phased Nutrition Plans</li>
      <li>Designated Accountability Coach</li>
      <li>Weekly accountability check in’s</li>
      <li>Weekly BodyScope Scans</li>
      <li>Exclusive Supplement Discounts</li>
      <li>Exclusive access to FitKorva’s ClubSpace Page</li>
    </ul>
    <p class="price price--three"><span class="tick">&#8220;</span><span class="amount">$125</span> per week<span class="tick">&#8221;</span></p>
  </section>

  <footer class="footer">
    <p class="footer-offer">SAVE MORE - 10% discount if paid in full</p>
    <p class="footer-tagline">We are not a Boot Camp with “fitness classes” We are professional training facility with Full Fitness Programs that Deliver Results!</p>
  </footer>
</main>
</body>
</html>
```